Flier needed for parenting seminar

Hello! We need a 4 by 6 clubcard needed for an upcoming parenting seminar. Flier should be in color, good quality images, and be front/back.
We are looking for something fresh, eye-catching, and not generic. Thanks!
CLUBCARD FRONT:
Veltran Institute presents:
Hearthbound Parenting:
Growing Steadfast Homes
By Shaykh Idris Kamal Tarbusi
Sat & Sun
Oct 22 & 23, 2016
9am - 7pm
Location: ORB Samira Hall
4187 Marlow Blvd
Santa Clara, CA 95127
Seating is limited. Register now!
Www.VeltranInstitute.com
1-877-Veltra7
CLUBCARD BACK:
There are no guarantees in life as to raising children to be how they should. Indeed, even Noah (as) lost his son while the Pharaoh's wife was able to raise Moses (as). And while traditionally a woman rears the child, Zakariyah (as) was a man chosen to raise one. The variety of scenarios in the Quran cover all possibilities. It is therefore worth reflecting on them to gain insight and draw parenting lessons.
So come and explore the Quranic view and prophetic guidelines for raising children. We hope this course serves as a landmark for you to know best practices and tools available to you, rooted in Quranic wisdom as well as our own experiences.
Some topics:
- The ways of Quranic raising
- Tools & examples from The Book
- What not to do
- Truth vs wisdom
www.VeltranInstitute.com
1-877-Veltra7
Parents, ppl considering becoming parents, ppl studying child development
- Fresh
- Eye-catching, not generic.
- Silhouette of mother/father with a young child.
- Maybe even praying together...

```html
<!DOCTYPE html>
<html lang="en">
<head>
<meta charset="utf-8">
<title>Parenting Seminar Clubcard</title>
<link href="https://fonts.googleapis.com/css2?family=Oswald:wght@500;600&family=Roboto+Condensed:wght@300;400&family=Sniglet:wght@800&display=swap" rel="stylesheet">
<style>
  :root {
    --bg: #e9e6ee;
    --navy: #26286a;
    --lavender: #9c99d6;
    --lavender-pale: #c9c7ee;
    --red: #e3141b;
    --ink: #222222;
    --white: #ffffff;
  }
  * { margin: 0; padding: 0; box-sizing: border-box; }
  html, body { width: 1200px; height: 1200px; overflow: hidden; background: var(--bg); }
  .card {
    position: absolute; width: 478px; height: 718px; background: var(--white);
    overflow: hidden; box-shadow: 0 6px 18px rgba(0,0,0,0.18);
    font-family: "Roboto Condensed", sans-serif;
  }
  .card--front { left: 114px; top: 205px;
    background: linear-gradient(180deg, var(--lavender-pale) 0%, #e6e5f7 30%, var(--white) 48%); }
  .card--back { left: 642px; top: 286px; }
  .brand {
    position: absolute; left: 0; right: 0; text-align: center;
    font-family: "Roboto Condensed", sans-serif; font-weight: 400; color: var(--navy);
  }
  .card--front .brand { top: 52px; font-size: 30px; letter-spacing: 1px; }
  .photo { position: absolute; }
  .photo--front {
    left: 0; top: 183px; width: 478px; height: 168px;
    background: linear-gradient(180deg, rgba(240,210,190,0.6) 0%, #d9b8a6 45%, #9fc3e6 75%, #e8b7d2 100%);
    clip-path: polygon(0 20%, 100% 20%, 100% 88%, 88% 100%, 12% 100%, 0 96%);
  }
  .title {
    position: absolute; left: 0; right: 0; top: 320px; text-align: center;
    font-family: "Sniglet", sans-serif; font-weight: 800; font-size: 39px; color: var(--navy);
  }
  .subtitle {
    position: absolute; left: 0; right: 0; top: 390px; text-align: center;
    font-family: "Oswald", sans-serif; font-weight: 600; font-size: 28px; line-height: 40px; color: var(--red);
  }
  .when {
    position: absolute; left: 0; right: 0; top: 490px; text-align: center;
    font-weight: 300; font-size: 30px; line-height: 35px; color: var(--ink);
  }
  .band { position: absolute; left: 0; width: 478px; }
  .card--front .band { top: 585px; height: 133px; }
  .card--back .band { top: 540px; height: 178px; }
  .location {
    position: absolute; left: 0; right: 0; top: 643px; text-align: center;
    font-size: 19px; line-height: 24px; color: var(--white);
  }
  .intro {
    position: absolute; left: 34px; top: 34px; width: 414px;
    font-size: 14.6px; line-height: 19.2px; color: var(--ink); text-align: justify;
  }
  .intro p + p { margin-top: 20px; }
  .topics-heading {
    position: absolute; left: 34px; top: 276px;
    font-family: "Oswald", sans-serif; font-weight: 600; font-size: 29px; color: var(--navy);
  }
  .topics { position: absolute; left: 34px; top: 323px; list-style: none; }
  .topics li { font-size: 21px; height: 35px; color: var(--ink); display: flex; align-items: center; gap: 6px; }
  .topics svg { width: 18px; height: 16px; }
  .photo--back {
    left: 172px; top: 312px; width: 306px; height: 250px;
    background: linear-gradient(120deg, #f3dccd 0%, #e8c9b1 35%, #f4e58a 65%, #ef8f8f 100%);
    clip-path: polygon(35% 0, 100% 12%, 100% 100%, 0 100%, 0 62%);
  }
  .card--back .brand { top: 582px; font-size: 17px; color: #d9d6ff; }
  .cta {
    position: absolute; left: 0; right: 0; top: 612px; text-align: center;
    font-family: "Oswald", sans-serif; font-weight: 600; font-size: 23px; color: var(--white);
  }
  .contact {
    position: absolute; left: 0; right: 0; top: 646px; text-align: center;
    font-size: 19px; line-height: 24px; color: var(--white);
  }
</style>
</head>
<body>
  <section class="card card--front">
    <div class="brand">Veltran Institute</div>
    <div class="photo photo--front" role="img" aria-label="Photo of a smiling family of four lying together"></div>
    <h1 class="title">Parenting Seminar</h1>
    <div class="subtitle">Growing Steadfast Homes<br>By Shaykh Idris Kamal Tarbusi</div>
    <div class="when">Sat &amp; Sun<br>Oct 22 &amp; 23, 2016<br>9am - 7pm</div>
    <svg class="band" viewBox="0 0 478 133" preserveAspectRatio="none">
      <path d="M0 40 Q260 30 478 0 L478 133 L0 133 Z" fill="var(--lavender)"/>
      <path d="M0 48 Q260 38 478 10 L478 133 L0 133 Z" fill="var(--navy)"/>
    </svg>
    <div class="location">Location : ORB Samira Hall<br>4187 Marlow Blvd, Santa Clara, CA 95127</div>
  </section>

  <section class="card card--back">
    <div class="intro">
      <p>There are no guarantees in life as to raising children to be how they should. Indeed, even Noah (as) lost his son while the Pharaoh's wife was able to raise Moses (as). And while traditionally a woman rears the child, Zakariyah (as) was a man chosen to raise one. The variety of scenarios in the Quran cover all possibilities. It is therefore worth reflecting on them to gain insight and draw parenting lessons.</p>
      <p>So come and explore the Quranic view and prophetic guidelines for raising children. We hope this course serves as a landmark for you to know best practices and tools available to you, rooted in Quranic wisdom as well as our own experiences.</p>
    </div>
    <h2 class="topics-heading">Some Topics</h2>
    <div class="photo photo--back" role="img" aria-label="Photo of a happy family of four hugging"></div>
    <ul class="topics">
      <li><svg viewBox="0 0 18 16"><path d="M1 9 L6 14 L17 1" fill="none" stroke="var(--navy)" stroke-width="3"/></svg>The ways of Quranic raising</li>
      <li><svg viewBox="0 0 18 16"><path d="M1 9 L6 14 L17 1" fill="none" stroke="var(--navy)" stroke-width="3"/></svg>Tools &amp; examples from The Book</li>
      <li><svg viewBox="0 0 18 16"><path d="M1 9 L6 14 L17 1" fill="none" stroke="var(--navy)" stroke-width="3"/></svg>What not to do</li>
      <li><svg viewBox="0 0 18 16"><path d="M1 9 L6 14 L17 1" fill="none" stroke="var(--navy)" stroke-width="3"/></svg>Truth vs wisdom</li>
    </ul>
    <svg class="band" viewBox="0 0 478 178" preserveAspectRatio="none">
      <path d="M0 38 Q240 -10 478 16 L478 178 L0 178 Z" fill="var(--lavender)"/>
      <path d="M0 48 Q240 2 478 28 L478 178 L0 178 Z" fill="var(--navy)"/>
    </svg>
    <div class="brand">Veltran Institute</div>
    <div class="cta">Seating is limited. Register now!</div>
    <div class="contact">www.VeltranInstitute.com<br>1-877-Veltra7</div>
  </section>
</body>
</html>
```